Design artwork for charcoal package

SOMEONE WILL BE AWARDED!!! MUST HAVE THE DESIGN BEFORE SUNDAY!!!
Don't forget to see the attachments.
The artwork is only for one side of the package. It can be in full colour. What to be written on the package will be provided after the award, but example packages are attached. The bag will be pp.
The dimension for the package are:
5kg bags are 60x40cm
8kg bags are 70x47cm
The logo is attached. Write: German Made and flag of Germany beside it. That part is a must and the logo of course.

The design must in away, so you use for different sizes.
More details will be provided what exact writing to be on the package when you be awarded. It means after you be rewarded, you must provide unlimited revisions. You must provide all the files such as Ai, PDF, png, etc. and copyright

Looking forward to your creative designs.

```html
<!DOCTYPE html>
<html lang="en">
<head>
<meta charset="utf-8">
<title>Stonewood Charcoal 5kg – Package Front</title>
<link href="https://fonts.googleapis.com/css2?family=Lato:wght@400;700;900&display=swap" rel="stylesheet">
<style>
  :root {
    --stage: #1e2318;
    --paper: #ecede7;
    --ink: #1c1f1a;
    --forest: #1f5a1e;
    --leaf: #8cc63f;
    --leaf-light: #a6d45a;
    --coal-dark: #141414;
    --coal-mid: #3a3a3a;
    --white: #ffffff;
  }
  * { margin: 0; padding: 0; box-sizing: border-box; }
  html, body { width: 1200px; height: 847px; overflow: hidden; }
  body {
    background: var(--stage);
    font-family: "Lato", sans-serif;
    position: relative;
  }
  .package-front {
    position: absolute;
    left: 350px; top: 44px;
    width: 500px; height: 760px;
    background: var(--paper);
    overflow: hidden;
  }
  .seal-line {
    position: absolute; left: 0; right: 0; top: 122px;
    height: 2px; background: var(--ink);
  }
  .brand {
    position: absolute; top: 136px; left: 0; right: 0;
    display: flex; flex-direction: column; align-items: center; gap: 3px;
  }
  .brand-dot {
    width: 22px; height: 22px; border-radius: 50%;
    border: 2px solid var(--leaf);
  }
  .brand-name {
    font-weight: 900; font-size: 15px; letter-spacing: 1px;
    color: var(--leaf);
  }
  .product-name {
    position: absolute; top: 188px; left: 0; right: 0;
    text-align: center;
    font-weight: 900; font-size: 54px; letter-spacing: 1px;
    color: var(--ink);
  }
  .product-type {
    position: absolute; top: 256px; left: 0; right: 0;
    text-align: center; line-height: 1.05;
    font-weight: 900; font-size: 34px; color: var(--ink);
  }
  .product-type .weight { display: block; font-size: 30px; }
  .flame-window {
    position: absolute; left: 0; top: 340px;
    width: 500px; height: 290px;
  }
  .natural-badge {
    position: absolute; left: 420px; top: 532px;
    width: 68px; height: 68px; border-radius: 50%;
    background: var(--white);
    border: 5px solid var(--leaf);
    display: flex; flex-direction: column; align-items: center; justify-content: center;
    color: var(--forest);
  }
  .natural-badge .pct { font-weight: 900; font-size: 15px; line-height: 1; }
  .natural-badge .word { font-weight: 700; font-size: 9px; }
  .origin-band {
    position: absolute; left: 0; right: 0; top: 630px; height: 130px;
    background: linear-gradient(180deg, var(--leaf-light), var(--leaf));
    display: flex; align-items: center; padding-left: 62px; gap: 8px;
  }
  .origin-text {
    color: var(--white); font-weight: 400; font-size: 26px; letter-spacing: 0.5px;
  }
  .flag { display: block; }
</style>
</head>
<body>
  <main class="package-front">
    <div class="seal-line"></div>

    <div class="brand">
      <span class="brand-dot"></span>
      <span class="brand-name">EMBERLY</span>
    </div>

    <h1 class="product-name">STONEWOOD</h1>
    <p class="product-type">Charcoal<span class="weight">5kg</span></p>

    <svg class="flame-window" viewBox="0 0 500 290" role="img" aria-label="Photo of lump charcoal pieces inside a flame-shaped window">
      <defs>
        <linearGradient id="coal" x1="0" y1="0" x2="1" y2="1">
          <stop offset="0" stop-color="#2b2b2b"/>
          <stop offset="0.5" stop-color="#1a1a1a"/>
          <stop offset="1" stop-color="#333333"/>
        </linearGradient>
      </defs>
      <path d="M0 80 C40 60 95 40 125 10 C150 60 210 80 260 95 C285 102 305 110 310 115 C320 70 335 40 345 25 C375 60 440 75 500 100 L500 290 L0 290 Z"
            fill="url(#coal)" stroke="var(--forest)" stroke-width="12" stroke-linejoin="round"/>
    </svg>

    <div class="natural-badge">
      <span class="pct">100%</span>
      <span class="word">Natural</span>
    </div>

    <div class="origin-band">
      <span class="origin-text">Made in Germany</span>
      <svg class="flag" width="30" height="18" viewBox="0 0 3 2" aria-label="Flag of Germany" role="img">
        <rect width="3" height="0.667" y="0" fill="#000000"/>
        <rect width="3" height="0.667" y="0.667" fill="#dd0000"/>
        <rect width="3" height="0.667" y="1.333" fill="#ffce00"/>
      </svg>
    </div>
  </main>
</body>
</html>
```